Pell School of Dental Assisting needs a WP (re)design.

We need a colorful Wordpress design for a relaunch of an old website. The relaunch is already underway and the website is live. The home page URL is brindlecrestacademy.example I have just completed a ArtFlock logo and the new logo is live on the website also. The installed Wordpress theme that is being used is Loomer III Plus with their "Talvek" subtheme. I would like a (re)design using the colors that are currently being represented by the new logo, and any additional complimentary colors. The information regarding the business can be found on the website already, so please review it for insight. The name of the business is "R. Jon Pell School of Dental Assisting".

Target Market(s)

The targeted website viewer is an adult female between the ages of 18 and 30 who is interested in attending our short term 10 week career school. The targeted audience's perception is two fold. Number one, they must have or develop interest in a future healthcare career and number two, they must complete the necessary requirements of our 10 week training course.

This website should inspire in the target viewer both the benefits of dental assistant employment and the essential learning and skills training required. Many of these potential student candidates are desperately wanting to get a job with income.

In addition to the hope of future employment, the website must represent the schools objectives are, classroom education and hands on clinical trainingl. Each webpage must represent both of these meanings to the targeted potential student.

Industry/Entity Type

Business

Font styles to use
Sans Serif

Requirements
Must have
• The phone number placed in a visible and high value widget area that allows mobile phone browser dialing.

```html
<!DOCTYPE html>
<html lang="en">
<head>
<meta charset="utf-8">
<title>R. Jon Pell School of Dental Assisting – Learn How to Become a Dental Assistant</title>
<link rel="stylesheet" href="https://fonts.googleapis.com/css2?family=Arimo:wght@400;700&display=swap">
<style>
:root{
  --page-bg:#17466f;
  --brand-blue:#1f78c1;
  --brand-dark:#14548d;
  --nav-blue:#1466ad;
  --heading-blue:#1a6fbb;
  --link-blue:#1b73c2;
  --ink:#222;
  --muted-ink:#1c3f66;
  --white:#fff;
  --green:#1f9a46;
  --call-green:#7cbf2b;
  --rule:#2a6aa6;
}
*{box-sizing:border-box;margin:0;padding:0}
html,body{width:1200px;height:1079px;overflow:hidden}
body{background:var(--page-bg);font-family:"Arimo",Arial,sans-serif;color:var(--ink);position:relative}
.site{position:absolute;left:179px;top:17px;width:866px;height:1062px;background:var(--brand-blue);border-radius:14px 14px 0 0;overflow:hidden}

/* header */
.site-header{position:absolute;left:0;top:0;width:866px;height:194px}
.nav-band{position:absolute;left:0;top:137px;width:866px;height:40px;background:var(--nav-blue)}
.brand{position:absolute;left:22px;top:40px;display:flex;align-items:center;gap:12px}
.brand-mark{width:40px;height:40px;background:var(--white);border-radius:50%;flex:none}
.brand-name{color:var(--white);font-weight:700;font-size:30px;line-height:34px;width:330px}
.social{position:absolute;display:flex;gap:17px}
.social span{width:29px;height:29px;border-radius:50%;background:var(--white);display:block}
.social.top{right:14px;top:13px}
.contact-block{position:absolute;right:13px;top:66px;text-align:right;color:var(--muted-ink);letter-spacing:.6px;font-style:normal}
.contact-block strong{display:block;font-size:16px;font-weight:700}
.contact-block span{display:block;font-size:12px;line-height:15px}
.main-nav{position:absolute;right:14px;top:149px;color:var(--white);font-size:14px;letter-spacing:1px}
.main-nav a{color:var(--white);text-decoration:none}
.main-nav i{font-style:normal;margin:0 9px}

/* banner */
.banner{position:absolute;left:10px;top:190px;width:846px;height:169px;background:var(--white);border:1px solid #0f3c66;display:flex}
.banner-photo{width:395px;height:100%;background:linear-gradient(90deg,#2a9d8f 0%,#b9a89b 45%,#e6e6e6 100%)}
.banner-copy{padding:22px 0 0 20px;color:var(--heading-blue)}
.banner-copy .lead{font-size:30px;line-height:34px}
.banner-copy .big{font-size:32px;font-weight:700;line-height:38px}
.banner-copy .sub{color:#222;font-size:16px;margin-top:12px;letter-spacing:.5px}
.banner-copy em{display:block;color:#333;font-size:14.5px;margin-top:6px;letter-spacing:.5px}

/* content */
.content-area{position:absolute;left:10px;top:371px;width:846px;height:651px;background:var(--white)}
.main-col{position:absolute;left:19px;top:0;width:600px}
.page-title{font-weight:400;font-size:22px;letter-spacing:.8px;padding:20px 0 12px 10px;border-bottom:1px solid var(--rule);color:#222;width:566px}
.intro{position:absolute;left:10px;top:74px;width:385px}
.intro h2{color:var(--heading-blue);font-size:19px;letter-spacing:.4px}
.intro .question{color:var(--link-blue);font-size:13.5px;line-height:17px;margin-top:9px}
.intro p{font-size:13.5px;line-height:16.5px;text-align:justify;margin-top:17px}
.intro .cta-line{color:var(--link-blue);text-align:left;margin-left:9px}
.founder-photo{position:absolute;left:436px;top:76px;width:182px;height:296px;border:2px solid var(--link-blue);background:linear-gradient(180deg,#8a8f6f 0%,#c9cfd6 40%,#eef1f4 100%)}
.points{position:absolute;left:19px;top:398px;list-style:none;font-size:13px;line-height:21.5px;letter-spacing:.3px;white-space:nowrap}
.goal{position:absolute;left:10px;top:518px;width:580px;color:var(--green);font-size:15px;line-height:17px;letter-spacing:.4px;text-align:center}

/* sidebar */
.sidebar{position:absolute;left:641px;top:4px;width:200px}
.widget{background:var(--brand-blue);margin-bottom:8px;color:var(--white)}
.call-widget{text-align:center;padding:10px 0 8px;height:119px}
.call-widget .call{font-size:22px;font-weight:700}
.call-widget .phone{font-size:22px;font-weight:700;letter-spacing:1px;color:var(--white);text-decoration:none;display:block}
.call-widget .more{font-size:13px}
.call-btn{display:inline-flex;align-items:center;gap:8px;margin-top:5px;background:var(--call-green);color:var(--white);font-weight:700;font-size:13px;padding:4px 10px 4px 6px;border-radius:3px;text-decoration:none}
.call-btn svg{display:block}
.form-widget{padding:7px 7px 9px;height:57px}
.form-widget label{font-size:13px;letter-spacing:.5px;display:block;margin-bottom:5px}
.form-row{display:flex;align-items:center;gap:8px}
.form-row input{width:156px;height:20px;border:none}
.widget-title{background:var(--brand-blue);color:var(--white);font-size:13px;letter-spacing:1px;padding:10px 10px;height:35px}
.link-list{list-style:none;padding:16px 0 4px 10px;border-left:1px solid var(--link-blue)}
.link-list li{position:relative;padding-left:16px;font-size:12.5px;line-height:15px;margin-bottom:18px;color:var(--link-blue)}
.link-list li::before{content:"";position:absolute;left:0;top:5px;width:6px;height:6px;border-radius:50%;background:var(--link-blue)}
.recent{padding-top:16px}
.recent li{margin-bottom:11px}

/* footer */
.site-footer{position:absolute;left:0;top:1024px;width:866px;height:38px;background:var(--brand-dark);color:var(--white);font-size:11px;letter-spacing:.6px;padding:12px 15px}
.social.bottom{right:14px;top:5px}
</style>
</head>
<body>
<div class="site">
  <header class="site-header">
    <div class="nav-band"></div>
    <div class="brand">
      <span class="brand-mark"></span>
      <span class="brand-name">R. Jon Pell School of Dental Assisting</span>
    </div>
    <div class="social top" aria-label="Social links"><span></span><span></span><span></span><span></span></div>
    <address class="contact-block">
      <strong>R. Jon Pell School of Dental Assisting</strong>
      <span>Larkspur Medical Plaza</span>
      <span>4820 Orchard Loop, Ste. 310 Fairbrook, TX 77000</span>
    </address>
    <nav class="main-nav">
      <a href="#">Home</a><i>|</i><a href="#">About Us</a><i>|</i><a href="#">Information</a><i>|</i><a href="#">Resources</a><i>|</i><a href="#">Contact Us</a>
    </nav>
  </header>

  <section class="banner">
    <div class="banner-photo" role="img" aria-label="Smiling dental assistant in teal scrubs in a dental clinic with a dentist behind her"></div>
    <div class="banner-copy">
      <div class="lead">Learn How to</div>
      <div class="big">Become a Dental Assistant</div>
      <div class="sub">In just 10 Weeks on Saturdays Only</div>
      <em>50% Classroom and 50% Hands On Clinical Training</em>
    </div>
  </section>

  <main class="content-area">
    <div class="main-col">
      <h1 class="page-title">R. Jon Pell School of Dental Assisting</h1>
      <div class="intro">
        <h2>Your Shortcut to a Meaningful Career!</h2>
        <p class="question">Would you believe that in only ten weekends you could learn the necessary skills to become a Dental Assistant?</p>
        <p>Everywhere in America and abroad, dental assistants jobs are in high demand. &nbsp;In both urban and rural areas dental assistants are being hired and paid well.</p>
        <p>If you are considering a career move, dental assisting may be right for you. Call us today because our next class begins soon and it's filling up very fast.</p>
        <p class="cta-line">Don't hesitate, call (555) 014-2290 now and sign up today.</p>
        <p>Located in Houston Texas, our career education course teaches each and every student the essential knowledge and skills that professional dental assistants must know to get a job.</p>
      </div>
      <div class="founder-photo" role="img" aria-label="School founder in a white lab coat, arms crossed, standing outdoors"></div>
      <ol class="points">
        <li>1.Students, are instructed in fundamental and general dental assisting.</li>
        <li>2.Approximately half of each session is in a classroom environment.</li>
        <li>3.In the other half of each session students participate and gain hands-on training.</li>
        <li>4.Instructor demonstration, coaching and evaluation make the experience fun.</li>
        <li>5.Requirements to become a registered dental assistant in the state of Texas are given.</li>
      </ol>
      <p class="goal">“Our goal is to help students gain fundamental dental assisting knowledge and hands-on clinical experience aimed at career placement and job satisfaction.”</p>
    </div>

    <aside class="sidebar">
      <div class="widget call-widget">
        <div class="call">Call</div>
        <a class="phone" href="tel:+15550142290">(555) 014-2290</a>
        <div class="more">for More Information</div>
        <a class="call-btn" href="tel:+15550142290">
          <svg width="18" height="18" viewBox="0 0 18 18"><rect width="18" height="18" rx="3" fill="#fff"/><path d="M6 4c-1 1-1 3 1 6s4 4 5 3l1-1-2-2-1 1c-1 0-3-2-3-3l1-1-2-2z" fill="#6aa821"/></svg>
          CALL NOW
        </a>
      </div>
      <div class="widget form-widget">
        <label>Search</label>
        <div class="form-row"><input type="text" aria-label="Search">
          <svg width="20" height="20" viewBox="0 0 20 20"><circle cx="8" cy="8" r="5.5" fill="none" stroke="#39b54a" stroke-width="2.5"/><path d="M12 12l5 5" stroke="#39b54a" stroke-width="3"/></svg>
        </div>
      </div>
      <div class="widget form-widget">
        <label>Subscribe to our Newsletter</label>
        <div class="form-row"><input type="email" aria-label="Email">
          <svg width="22" height="18" viewBox="0 0 22 18"><path d="M0 6h11V1l10 8-10 8v-5H0z" fill="#39b54a"/></svg>
        </div>
      </div>
      <div class="widget-title">Pages</div>
      <ul class="link-list">
        <li>About R. Jon Pell School of Dental Assisting</li>
        <li>R. Jon Pell School<br>of Dental Assisting</li>
        <li>Contact R. Jon Pell School of Dental Assisting</li>
        <li>Dental Assistant Resources</li>
        <li>Dental Assistant School Information</li>
      </ul>
      <div class="widget-title">Recent Post</div>
      <ul class="link-list recent">
        <li>Hello world!</li>
        <li>Hello world!</li>
      </ul>
    </aside>
  </main>

  <footer class="site-footer">
    © 2014 - Learn How to Become a Dental Assistant
    <div class="social bottom" aria-label="Social links"><span></span><span></span><span></span><span></span></div>
  </footer>
</div>
</body>
</html>
```